MORIVO VEGAN SUSHI

www.morivo-restaurant.de
We are open in 2018 and are an innovative restaurant from Munich. We would like a cool design for our drinks and food menu. It's very simple at the moment. See the File menu. In any case, our logo should appear. On the website we use neutraface as a font. But it's not a must. We are only open in the evening and appeal to a young, upscale audience.

```html
<!DOCTYPE html>
<html lang="de">
<head>
<meta charset="utf-8">
<title>MORIVO Speisekarte</title>
<link rel="stylesheet" href="https://fonts.googleapis.com/css2?family=Mulish:ital,wght@0,300;0,400;0,700;0,800;1,400&family=Shojumaru&display=swap">
<style>
  :root {
    --ink: #141414;
    --sea: #0a6f9b;
    --salmon: #f6a074;
    --sand: #efd9c2;
    --leaf: #2a7a2e;
    --paper: #ffffff;
    --frame: #b9b9b9;
  }
  * { box-sizing: border-box; margin: 0; padding: 0; }
  html, body { width: 1200px; height: 823px; overflow: hidden; background: var(--paper); }
  body { position: relative; font-family: "Mulish", sans-serif; color: var(--ink); }

  .menu-page {
    position: absolute; top: 18px; width: 555px; height: 784px;
    border: 1px solid var(--frame); overflow: hidden; background: var(--paper);
  }
  .menu-page--sets { left: 19px; }
  .menu-page--carte { left: 627px; }

  .page-art { position: absolute; inset: 0; width: 100%; height: 100%; }

  .brand {
    position: absolute; top: 118px; left: 0; width: 100%;
    text-align: center; font-weight: 300; font-size: 24px;
    letter-spacing: 15px; padding-left: 15px; line-height: 30px;
  }

  .block { position: absolute; text-align: center; line-height: 15px; font-size: 11.4px; }
  .block--center { left: 0; width: 555px; }
  .block--col { width: 180px; }
  .block--left { text-align: left; width: 260px; }

  .heading {
    font-family: "Shojumaru", cursive; font-weight: 400; color: var(--sea);
    font-size: 16px; line-height: 18px; letter-spacing: 0.5px; white-space: nowrap;
  }
  .line { white-space: nowrap; }
  .line em { font-style: italic; }
  .line b { font-weight: 700; }
  .price { font-size: 15.5px; line-height: 20px; margin-top: 1px; font-weight: 400; }

  .vegan-note { position: absolute; left: 25px; top: 720px; }
  .vegan-note strong {
    display: block; color: var(--leaf); font-weight: 800; font-size: 12px; line-height: 16px;
  }
  .vegan-note span {
    display: block; font-style: italic; font-size: 8px; line-height: 11px;
  }
</style>
</head>
<body>

<!-- Seite 1: Menüs & Sets -->
<article class="menu-page menu-page--sets">
  <svg class="page-art" viewBox="0 0 1073 1517" preserveAspectRatio="none" aria-hidden="false">
    <polygon points="318,0 1073,0 1073,120 838,215" fill="var(--salmon)"/>
    <polygon points="838,215 1073,120 1073,315" fill="var(--sand)" role="img" aria-label="Japanisches Asanoha-Muster in Sandtönen"/>
    <polygon points="0,0 393,0 0,195" fill="var(--sea)" role="img" aria-label="Japanisches Wellenmuster in Blau"/>
    <polygon points="0,1197 233,1293 0,1385" fill="var(--sand)" role="img" aria-label="Japanisches Asanoha-Muster in Sandtönen"/>
    <polygon points="0,1385 233,1293 773,1517 0,1517" fill="var(--salmon)"/>
    <polygon points="1073,1310 1073,1517 573,1517" fill="var(--sea)" role="img" aria-label="Japanisches Wellenmuster in Blau"/>
  </svg>

  <div class="brand">MORIVO</div>

  <section class="block block--center" style="top:184px">
    <h2 class="heading">CHEF MENÜ MIT APERITIV</h2>
    <p class="line"><em>für 2 Personen</em></p>
    <p class="line">Kleine Portion RAMENSUPPE <em>mit Gemüse &amp; Nudeln</em></p>
    <p class="line">MINI SET</p>
    <p class="line">DESSERT</p>
    <p class="price">81,00€</p>
  </section>

  <section class="block block--center" style="top:302px">
    <h2 class="heading">OMAKASE</h2>
    <p class="line" style="line-height:13.5px"><em>für 2 Personen</em></p>
    <p class="line" style="line-height:13.5px">EDAMAME</p>
    <p class="line" style="line-height:13.5px">OMAKASE SET <em>mit 8 Spezialitäten des Hauses</em></p>
    <p class="line" style="line-height:13.5px">PANA COTTA <em>mit Beeren</em></p>
    <p class="price">68,00€</p>
  </section>

  <section class="block block--col" style="top:418px;left:7px">
    <h2 class="heading">SET 1</h2>
    <p class="line">HOSOMAKI</p>
    <p class="line">FUTOMAKI</p>
    <p class="line">NIGIRI</p>
    <p class="line">KÜRBISKROKETTEN</p>
    <p class="line">WAKAME GURKEN SALAT</p>
    <p class="line">PICKLES</p>
    <p class="line">GYOZA TEIGTASCHEN</p>
    <p class="line">SUSHI CAKE</p>
    <p class="price">33,90€</p>
  </section>

  <section class="block block--col" style="top:419px;left:183px">
    <h2 class="heading">SET 2</h2>
    <p class="line">HOSOMAKI</p>
    <p class="line">FUTOMAKI</p>
    <p class="line">PICKLES</p>
    <p class="line">SUSHI “THUNA” CAKE</p>
    <p class="line">Crispy AUBERGINEN <em>mit Mayo</em></p>
    <p class="line">AUBERGINE DENGAKU</p>
    <p class="price">31,90€</p>
  </section>

  <section class="block block--col" style="top:418px;left:360px">
    <h2 class="heading">SET 3</h2>
    <p class="line">HOSOMAKI</p>
    <p class="line">URAMAKI</p>
    <p class="line">NIGIRI</p>
    <p class="line">GEMÜSE TEMPURA</p>
    <p class="line">Crispy TOFUSTICKS <em>mit Mayo</em></p>
    <p class="line">WAKAME SHIRA AE</p>
    <p class="price">28,90€</p>
  </section>

  <footer class="vegan-note">
    <strong>All Vegan</strong>
    <span>Bitte teilen Sie dem Service unbedingt Allergien mit und</span>
    <span>fragen Sie nach&nbsp; der Allergiker-Menükarte</span>
  </footer>
</article>

<!-- Seite 2: Karte -->
<article class="menu-page menu-page--carte">
  <svg class="page-art" viewBox="0 0 1073 1517" preserveAspectRatio="none">
    <polygon points="318,0 1073,0 1073,120 838,215" fill="var(--salmon)"/>
    <polygon points="838,215 1073,120 1073,315" fill="var(--sand)" role="img" aria-label="Japanisches Asanoha-Muster in Sandtönen"/>
    <polygon points="0,0 393,0 0,195" fill="var(--sea)" role="img" aria-label="Japanisches Wellenmuster in Blau"/>
    <polygon points="0,1197 233,1293 0,1385" fill="var(--sand)" role="img" aria-label="Japanisches Asanoha-Muster in Sandtönen"/>
    <polygon points="0,1385 233,1293 773,1517 0,1517" fill="var(--salmon)"/>
    <polygon points="1073,1310 1073,1517 573,1517" fill="var(--sea)" role="img" aria-label="Japanisches Wellenmuster in Blau"/>
  </svg>

  <div class="brand">MORIVO</div>

  <section class="block block--center" style="top:173px">
    <h2 class="heading">VORSPEISEN</h2>
    <p class="line">MISO SUPPE <b>5,50€</b></p>
    <p class="line">EDAMAME MIT SALZ/CHILI <b>4,50€</b></p>
    <p class="line">SEIDENTOFU in hausgemachter Sauce mit Mandeln <b>5,50€</b></p>
  </section>

  <section class="block block--left" style="top:258px;left:44px">
    <h2 class="heading">SUSHI</h2>
    <p class="line">URAMAKI mit Tempuragemüse <b>8,90€</b></p>
    <p class="line">FUTOMAKI wechselndes Gemüse <b>8,00€</b></p>
    <p class="line">URAMAKI mit Austernpilze <b>7,50€</b></p>
    <p class="line">HOSOMAKI Gurke Avocado <b>5,50€</b></p>
    <p class="line">HOSOMAKI Gurke Shiitake <b>5,50€</b></p>
    <p class="line">TOMATEN NIGIRI <b>4,50€</b></p>
  </section>

  <section class="block block--left" style="top:258px;left:286px">
    <h2 class="heading">KLEINE GERICHTE</h2>
    <p class="line">GEMÜSE TEMPURA <b>8,00€</b></p>
    <p class="line">Crispy TOFUSTICKS mit Mayo <b>8,00€</b></p>
    <p class="line">KÜRBISKROKETTEN mit TANGASHU <b>7,90€</b></p>
    <p class="line">SUSHI “THUNA” CAKE <b>6,90€</b></p>
    <p class="line">SUSHI CAKE CLASSIC <b>6,00€</b></p>
    <p class="line">AUBERGINE DENGAKU <b>5,50€</b></p>
  </section>

  <section class="block block--center" style="top:389px">
    <h2 class="heading">HAUPTSPEISEN</h2>
    <p class="line">Herrlich cremiges KATSU CURRY mit knusprigen Auberginensticks, Reis &amp; Pickles</p>
    <p class="price">17,90€</p>
  </section>

  <section class="block block--center" style="top:454px">
    <p class="line">RAMEN SUPPE mit Nudeln, Gemüse &amp; Tofu</p>
    <p class="price">14,90€</p>
  </section>

  <section class="block block--center" style="top:499px">
    <p class="line">CHIRASHI SUSHI BOWL</p>
    <p class="price">13,90€</p>
  </section>

  <section class="block block--center" style="top:545px">
    <p class="line">SOMMERSALATE mit Sesamdressing &amp; crispy Tofusticks mit Mayo</p>
    <p class="price">12,50€</p>
  </section>

  <section class="block block--center" style="top:599px">
    <h2 class="heading">DESSERT</h2>
    <p class="line">CHEESECAKE mit Beeren <b>6,50€</b></p>
    <p class="line">PANA COTTA mit Beeren <b>5,90€</b></p>
    <p class="line">SORBET des Tages <b>5,50€</b></p>
    <p class="line">SORBET des Tages mit Schuss <b>6,90€</b></p>
  </section>

  <footer class="vegan-note">
    <strong>All Vegan</strong>
    <span>Bitte teilen Sie dem Service unbedingt Allergien mit und</span>
    <span>fragen Sie nach&nbsp; der Allergiker-Menükarte</span>
  </footer>
</article>

</body>
</html>
```